Corvana Wound Care Business card design

We need a business card designed around our logo which was provided. The logo of preference is the colored. Also the colors and fonts were provided.

Target Market(s)

Our Referral partners are home health agencies.

Industry/Entity Type

Healthcare

Contact Information for Business Card

Name , Phone #, Email , Title

Requirements
Nice to have
• Creativity
Should not have
• basic

```html
<!DOCTYPE html>
<html lang="en">
<head>
<meta charset="utf-8">
<title>Corvana Wound Care – Business Card</title>
<link href="https://fonts.googleapis.com/css2?family=Libre+Caslon+Text:wght@400;700&family=Montserrat:wght@400;500;600&display=swap" rel="stylesheet">
<style>
  :root {
    --page-bg: #d3d4d8;
    --card-white: #ffffff;
    --brand-navy: #0e4a8f;
    --brand-blue: #1a5fb4;
    --brand-deep: #0c3f7e;
    --pattern-dark: #173a73;
    --pattern-light: #5d86b8;
    --text-grey: #4a4d52;
    --rule-blue: #7fb2e0;
  }
  * { box-sizing: border-box; margin: 0; padding: 0; }
  html, body { width: 1200px; height: 788px; overflow: hidden; }
  body {
    background: var(--page-bg);
    font-family: "Montserrat", Arial, sans-serif;
    position: relative;
  }
  .card {
    position: absolute;
    top: 234px;
    width: 560px;
    height: 320px;
    border-radius: 18px;
    overflow: hidden;
    box-shadow: 0 6px 18px rgba(0,0,0,0.18);
  }
  .card-front { left: 27px; background: var(--card-white); }
  .card-back { left: 613px; background: var(--brand-deep); }

  /* front */
  .front-brand {
    position: absolute;
    left: 30px;
    top: 40px;
    width: 70px;
    height: 240px;
    display: flex;
    flex-direction: column;
    align-items: center;
    justify-content: flex-end;
    gap: 12px;
  }
  .brand-name-vertical {
    writing-mode: vertical-rl;
    transform: rotate(180deg);
    font-family: "Montserrat", Arial, sans-serif;
    font-weight: 600;
    font-size: 19px;
    color: var(--brand-blue);
    white-space: nowrap;
  }
  .brand-dot {
    width: 20px; height: 20px;
    border-radius: 50%;
    background: var(--brand-blue);
  }
  .front-divider {
    position: absolute;
    left: 124px;
    top: 40px;
    width: 1.5px;
    height: 240px;
    background: linear-gradient(to bottom, transparent, var(--rule-blue) 15%, var(--rule-blue) 85%, transparent);
  }
  .contact-block {
    position: absolute;
    left: 156px;
    top: 52px;
    color: var(--text-grey);
    font-size: 13px;
    line-height: 1.55;
  }
  .person-name {
    font-family: "Libre Caslon Text", Georgia, serif;
    font-size: 24px;
    color: var(--brand-navy);
    letter-spacing: 0.5px;
    line-height: 1.1;
  }
  .person-title { font-size: 13px; margin-top: 2px; }
  .dash {
    width: 10px; height: 1.5px;
    background: var(--rule-blue);
    margin: 12px 0 10px;
  }
  .contact-list { list-style: none; }
  .contact-list li { display: flex; align-items: center; gap: 8px; }
  .contact-list svg { width: 12px; height: 12px; flex: none; }

  /* back */
  .back-pattern { position: absolute; inset: 0; width: 100%; height: 100%; }
  .back-brand {
    position: absolute;
    right: 46px;
    bottom: 70px;
    display: flex;
    align-items: center;
    gap: 12px;
  }
  .back-brand .brand-dot { width: 26px; height: 26px; background: #fff; }
  .brand-name {
    font-family: "Montserrat", Arial, sans-serif;
    font-weight: 600;
    font-size: 26px;
    color: #fff;
    white-space: nowrap;
  }
</style>
</head>
<body>

<section class="card card-front" aria-label="Card front">
  <div class="front-brand">
    <span class="brand-name-vertical">Corvana Wound Care</span>
    <span class="brand-dot"></span>
  </div>
  <div class="front-divider"></div>

  <div class="contact-block">
    <h1 class="person-name">DALEN MARSH</h1>
    <p class="person-title">CEO/Founder</p>
    <div class="dash"></div>
    <p>4410 Harlow Avenue, Suite 210<br>Brenton Falls, AB 55190</p>
    <div class="dash"></div>
    <ul class="contact-list">
      <li>
        <svg viewBox="0 0 12 12"><circle cx="6" cy="6" r="6" fill="var(--brand-navy)"/><path d="M4 3.2l1 1.4-.6.7c.4.8 1 1.4 1.8 1.8l.7-.6 1.4 1-.6 1c-2.5-.3-4.4-2.2-4.7-4.7z" fill="#fff"/></svg>
        555-318-2046
      </li>
      <li>
        <svg viewBox="0 0 12 12"><circle cx="6" cy="6" r="6" fill="var(--brand-navy)"/><rect x="3" y="4" width="6" height="4.2" fill="none" stroke="#fff" stroke-width=".9"/><path d="M3 4l3 2.3L9 4" fill="none" stroke="#fff" stroke-width=".9"/></svg>
        info@corvanawoundcare.com
      </li>
      <li>
        <svg viewBox="0 0 12 12"><circle cx="6" cy="6" r="6" fill="var(--brand-navy)"/><circle cx="6" cy="6" r="3.2" fill="none" stroke="#fff" stroke-width=".8"/><path d="M2.8 6h6.4M6 2.8c-1.5 1.8-1.5 4.6 0 6.4M6 2.8c1.5 1.8 1.5 4.6 0 6.4" fill="none" stroke="#fff" stroke-width=".7"/></svg>
        www.corvanawoundcare.com
      </li>
    </ul>
  </div>
</section>

<section class="card card-back" aria-label="Card back">
  <svg class="back-pattern" viewBox="0 0 560 320" preserveAspectRatio="none" role="img" aria-label="Decorative pattern of scattered cross shapes over deep blue">
    <defs>
      <linearGradient id="backTone" x1="0" y1="1" x2="1" y2="0">
        <stop offset="0" stop-color="#123a74"/>
        <stop offset="0.55" stop-color="#0f4b92"/>
        <stop offset="1" stop-color="#3e6ea8"/>
      </linearGradient>
    </defs>
    <rect width="560" height="320" fill="url(#backTone)"/>
  </svg>
  <div class="back-brand">
    <span class="brand-dot"></span>
    <span class="brand-name">Corvana Wound Care</span>
  </div>
</section>

</body>
</html>
```